Design letter head and business card

Hello,

you should design a business card and letter paper for Wolkenfalke Marketing. In German we write this word with K insteat of C.

Company does not have a logo. But in general, we write Wolkenfalke Marketing in 2 lines.
First line red: WOLKENFALKE
Second line gray: MARKETING

Red (or wine red) and Gray / Black are our favorite colors.

Company slogan: "Next Level Online Marketing".

Company offers SEO, SEM, SEA, AdWords, Conversion Optimization, Online Markting Consulting ...

The website is old, please do not use this as base for your task.

German letter paper sizes:
Viawable Dimensions : 210 x 297 mm
Needed file dimensions: 212 x 299 mm

Informations to include:

Address:
Wolkenfalke Marketing GmbH
Lindenweg 23
71384 Weinstadt
Germany

Geschäftsführer | CEO: Dietrich Ronnau

Phone: +49 (0) 7151 482 67 05

Fax: +49 (0) 7151 482 67 88

Mail: info@wolkenfalke-marketing.de

Web: www.wolkenfalke-marketing.de

Amtsgericht Suttgart, HRB 736402

Bank: Sonnfelder Bank
IBAN: DE139817325500XXXXXXXX
BIC: GENODES1QTR

Thanks

Dietrich

Target Market(s)

People who likes to win the online marketing game.

Industry/Entity Type

Business

Contact Information for Business Card

Here is the personal text on the card:

Name:
Dietrich Ronnau

Title:
Geschäftsführer | CEO

Address:
Wolkenfalke Marketing GmbH
Lindenweg 23
71384 Weinstadt
Germany

Phone:
+49 (0) 7151 482 67 05

Fax:
+49 (0) 7151 482 67 88

Mail:
ronnau@wolkenfalke-marketing.de

Web:
www.wolkenfalke-marketing.de

Business Card:
Viewable Dimensions: 85 x 55 mm
Needed file dimensions: 87 x 57mm

Font styles to use
Sans Serif

Requirements
Nice to have
• It would be great to see the dynamics of a helicopter.

```html
<!DOCTYPE html>
<html lang="de">
<head>
<meta charset="utf-8">
<title>Wolkenfalke Marketing – Visitenkarte</title>
<link rel="stylesheet" href="https://fonts.googleapis.com/css2?family=Jost:wght@400;600&display=swap">
<style>
  :root {
    --stage: #1c1c1c;
    --paper: #f7f7f7;
    --card-dark: #2f2f30;
    --brand-red: #b0102e;
    --ink-gray: #555557;
    --band-gray: #6b6b6d;
    --white: #ffffff;
  }
  * { margin: 0; padding: 0; box-sizing: border-box; }
  html, body { width: 1200px; height: 1000px; overflow: hidden; }
  body {
    position: relative;
    background: var(--stage);
    font-family: "Jost", "Century Gothic", sans-serif;
  }
  .card { position: absolute; width: 580px; height: 323px; overflow: hidden; }
  .card-front { left: 201px; top: 149px; background: var(--paper); }
  .card-back  { left: 420px; top: 549px; background: var(--card-dark); }

  .person { position: absolute; left: 41px; top: 46px; }
  .person-name { color: var(--brand-red); font-weight: 600; font-size: 20px; letter-spacing: 0.3px; line-height: 24px; }
  .person-title { color: var(--ink-gray); font-size: 15px; line-height: 20px; }

  .brand { position: absolute; display: flex; align-items: center; }
  .brand-mark { background: var(--brand-red); flex: none; }
  .brand-name { color: var(--brand-red); font-weight: 400; line-height: 1; text-transform: uppercase; }
  .brand-name span { display: block; }

  .card-front .brand { left: 289px; top: 49px; }
  .card-front .brand-mark { width: 50px; height: 50px; margin-right: 12px; }
  .card-front .brand-line1 { font-size: 29px; letter-spacing: 0.5px; }
  .card-front .brand-line2 { font-size: 18px; letter-spacing: 5.6px; margin-top: 5px; }

  .contacts { position: absolute; left: 41px; top: 209px; list-style: none; }
  .contacts li { display: flex; align-items: center; height: 18px; color: var(--ink-gray); font-size: 14px; }
  .contacts svg { width: 14px; height: 14px; margin-right: 8px; flex: none; }

  .address { position: absolute; right: 41px; top: 226px; text-align: right; color: var(--ink-gray); font-size: 14px; line-height: 18px; font-style: normal; }

  .accent-band { position: absolute; left: 0; bottom: 0; width: 580px; height: 13px; }

  .card-back .brand { left: 41px; top: 45px; }
  .card-back .brand-mark { width: 66px; height: 66px; margin-right: 16px; }
  .card-back .brand-line1 { font-size: 39px; letter-spacing: 0.5px; }
  .card-back .brand-line2 { font-size: 25px; letter-spacing: 8.4px; margin-top: 6px; }

  .slogan { position: absolute; left: 40px; top: 275px; font-size: 18px; color: var(--white); }
  .slogan em { font-style: normal; color: var(--brand-red); }
</style>
</head>
<body>
  <section class="card card-front" aria-label="Visitenkarte Vorderseite">
    <div class="person">
      <p class="person-name">JONAS ALBRECHT</p>
      <p class="person-title">Managing Director</p>
    </div>

    <div class="brand">
      <div class="brand-mark"></div>
      <p class="brand-name"><span class="brand-line1">Wolkenfalke</span><span class="brand-line2">Marketing</span></p>
    </div>

    <ul class="contacts">
      <li>
        <svg viewBox="0 0 14 14"><rect width="14" height="14" rx="2" fill="var(--brand-red)"/><path d="M4 3.5c.6-.5 1.2-.4 1.5.2l.6 1.2c.2.4 0 .8-.3 1l-.4.3c.4.9 1.1 1.6 2 2l.3-.4c.3-.3.7-.4 1-.2l1.2.6c.6.3.7.9.2 1.5-.6.7-1.5.8-2.3.4C6 9.3 4.7 8 3.9 6.2c-.4-.9-.5-1.9.1-2.7z" fill="#fff"/></svg>
        +49 (0) 7151 482 67 05
      </li>
      <li>
        <svg viewBox="0 0 14 14"><rect width="14" height="14" rx="2" fill="var(--brand-red)"/><rect x="4.5" y="2.8" width="5" height="3" fill="#fff"/><rect x="3" y="6" width="8" height="4" rx="0.6" fill="#fff"/><rect x="4.5" y="9" width="5" height="2.4" fill="#fff" stroke="var(--brand-red)" stroke-width="0.6"/></svg>
        +49 (0) 7151 482 67 88
      </li>
      <li>
        <svg viewBox="0 0 14 14"><rect width="14" height="14" rx="2" fill="var(--brand-red)"/><rect x="3" y="4" width="8" height="6" fill="#fff"/><path d="M3 4l4 3.2L11 4" fill="none" stroke="var(--brand-red)" stroke-width="0.9"/></svg>
        info@wolkenfalke-marketing.de
      </li>
      <li>
        <svg viewBox="0 0 14 14"><rect width="14" height="14" rx="2" fill="var(--brand-red)"/><g fill="none" stroke="#fff" stroke-width="0.9"><circle cx="7" cy="7" r="4"/><ellipse cx="7" cy="7" rx="1.7" ry="4"/><path d="M3 7h8"/></g></svg>
        www.wolkenfalke-marketing.de
      </li>
    </ul>

    <address class="address">
      Lindenweg 23<br>
      71384 Weinstadt<br>
      Germany
    </address>

    <svg class="accent-band" viewBox="0 0 580 13" preserveAspectRatio="none" aria-hidden="true">
      <polygon points="0,1 292,1 280,13 0,13" fill="var(--band-gray)"/>
      <polygon points="302,0 580,0 580,13 290,13" fill="var(--brand-red)"/>
    </svg>
  </section>

  <section class="card card-back" aria-label="Visitenkarte Rückseite">
    <div class="brand">
      <div class="brand-mark"></div>
      <p class="brand-name"><span class="brand-line1">Wolkenfalke</span><span class="brand-line2">Marketing</span></p>
    </div>
    <p class="slogan">Next Level <em>Online Marketing</em></p>
  </section>
</body>
</html>
```